Business card

I need a business card design for my consulting company in animal welfare for livestock. I like clean, crisp, simple.

One I imagined was double-sided:
side1: just my name and contact information
side2: silhouette of farm animals. Could be 3 (pig, cow, chicken) or all the species (pig, cow, chicken, duck, sheep, rabbit, etc) that continue the length of the card. I have attached an image of a silhouette style.

But, I am open to any concept.

Industry/Entity Type

Business

```html
<!DOCTYPE html>
<html lang="en">
<head>
<meta charset="utf-8">
<title>Consulting Company – Business Card</title>
<link href="https://fonts.googleapis.com/css2?family=Cabin:wght@400;500&display=swap" rel="stylesheet">
<style>
  :root {
    --backdrop: #e4ecea;
    --card: #f8f8f8;
    --accent: #f2512b;
    --ink: #151515;
    --rule: #b9b9b9;
    --silhouette: #1a1a1a;
    --silhouette-soft: #4a4a4a;
  }
  * { box-sizing: border-box; margin: 0; padding: 0; }
  html, body { width: 1200px; height: 675px; overflow: hidden; }
  body {
    background: var(--backdrop);
    font-family: "Cabin", "Gill Sans", sans-serif;
    color: var(--ink);
    display: flex;
    align-items: center;
    justify-content: center;
    gap: 50px;
  }
  .card {
    position: relative;
    width: 525px;
    height: 300px;
    background: var(--card);
    box-shadow: 3px 4px 8px rgba(0,0,0,.35);
    overflow: hidden;
  }
  .top-rule {
    position: absolute;
    top: 9px; left: 0; right: 0;
    height: 7px;
    background: var(--accent);
  }
  .bottom-band {
    position: absolute;
    left: 0; right: 0; bottom: 0;
    background: var(--accent);
  }
  /* front */
  .company {
    position: absolute;
    top: 108px; left: 0; right: 0;
    text-align: center;
    font-size: 27px;
    font-weight: 400;
    letter-spacing: .5px;
  }
  .designation {
    position: absolute;
    top: 146px; left: 0; right: 0;
    text-align: center;
    font-size: 14px;
    color: var(--accent);
  }
  .contacts {
    position: absolute;
    top: 224px; left: 0; right: 0;
    display: flex;
    justify-content: center;
    align-items: center;
    font-size: 14px;
  }
  .contact { display: flex; align-items: center; gap: 6px; padding: 0 18px; }
  .contact + .contact { border-left: 1px solid var(--rule); }
  .contact svg { width: 12px; height: 12px; fill: var(--ink); }
  .front .bottom-band {
    height: 44px;
    display: flex;
    align-items: center;
    justify-content: center;
    color: #fff;
    font-size: 14px;
  }
  /* back */
  .back .bottom-band { height: 38px; }
  .animals {
    position: absolute;
    left: 60px; right: 55px;
    top: 100px; height: 115px;
    background: linear-gradient(180deg, var(--card) 0%, var(--silhouette-soft) 40%, var(--silhouette) 100%);
    opacity: .85;
    border-radius: 4px;
  }
</style>
</head>
<body>
  <section class="card front">
    <div class="top-rule"></div>
    <h1 class="company">CONSULTING COMPANY</h1>
    <p class="designation">Desgination</p>
    <div class="contacts">
      <span class="contact">
        <svg viewBox="0 0 12 12" aria-hidden="true"><circle cx="6" cy="3.5" r="2.6"/><path d="M1 12c0-3 2.2-5 5-5s5 2 5 5z"/></svg>
        +00000000000
      </span>
      <span class="contact">
        <svg viewBox="0 0 12 12" aria-hidden="true"><path d="M3.5 0h5a1 1 0 0 1 1 1v10a1 1 0 0 1-1 1h-5a1 1 0 0 1-1-1V1a1 1 0 0 1 1-1zm.5 2v6h4V2z"/></svg>
        +0000000000
      </span>
      <span class="contact">
        <svg viewBox="0 0 12 12" aria-hidden="true"><path d="M0 2h12v8H0zm1.2 1.1v.3L6 6.6l4.8-3.2v-.3zm0 1.5V9h9.6V4.6L6 7.8z"/></svg>
        xyz@example.com
      </span>
    </div>
    <div class="bottom-band">Address: Lorem ipsum dolor sit amet, consectetur adipiscing elit</div>
  </section>

  <section class="card back">
    <div class="top-rule"></div>
    <div class="animals" role="img" aria-label="Black silhouettes of a chicken, a pig and a cow standing in a row, increasing in size"></div>
    <div class="bottom-band"></div>
  </section>
</body>
</html>
```